Business cards and stationery for business consulting company
Larkspur Holdings LLC
Business cards and stationery for business consulting company - Consulting
Creative Brief
Bright & Fun-filled
Tobias Ferrant Aldo
Chief Strategist
New York, USA.
tobias@lhllc.example
Per designed logo, please include 'Global Business Strategists'
quillmark-308 quillmark-308
where i can find your logo ? or i have to make it ?

```html
<!DOCTYPE html>
<html lang="en">
<head>
<meta charset="utf-8">
<title>Larkspur Holdings LLC — Business Cards</title>
<link rel="stylesheet" href="https://fonts.googleapis.com/css2?family=Open+Sans:wght@400;600&display=swap">
<style>
  :root {
    --stage: #3b3b3d;
    --navy: #0b1a66;
    --royal: #1d4fc4;
    --sky: #4fb6ee;
    --paper: #ffffff;
    --ink-blue: #1a2f9a;
    --ink-red: #c8102e;
    --ink-grey: #555a60;
    --rule: #8a8f96;
  }
  * { box-sizing: border-box; margin: 0; padding: 0; }
  html, body {
    width: 1200px; height: 750px; overflow: hidden;
    background: var(--stage);
    font-family: "Open Sans", Arial, sans-serif;
  }
  .sheet {
    position: relative; width: 1200px; height: 750px;
    display: flex; align-items: center; justify-content: center; gap: 44px;
  }
  .card {
    position: relative; width: 530px; height: 303px;
    border-radius: 18px; overflow: hidden;
    box-shadow: 0 14px 30px rgba(0,0,0,.45);
  }
  /* Back */
  .card--back {
    background: radial-gradient(ellipse 55% 60% at 50% 42%, var(--sky) 0%, var(--royal) 45%, var(--navy) 100%);
    display: flex; flex-direction: column; align-items: center; justify-content: center;
    color: var(--paper);
  }
  .back-mark { display: flex; align-items: center; gap: 12px; margin-top: -8px; }
  .back-mark__dot { width: 22px; height: 22px; border-radius: 50%; background: var(--paper); }
  .back-mark__name { font-size: 26px; font-weight: 600; letter-spacing: .5px; }
  .back-web { margin-top: 46px; font-size: 13px; letter-spacing: 4px; }
  /* Front */
  .card--front { background: var(--paper); }
  .front-disc {
    position: absolute; right: -40px; top: 24px; width: 250px; height: 250px; border-radius: 50%;
    background: radial-gradient(circle at 40% 40%, var(--sky), var(--royal) 60%, var(--navy));
  }
  .identity { position: absolute; left: 40px; top: 62px; }
  .identity__company {
    font-size: 18px; font-weight: 600; color: var(--ink-grey); letter-spacing: .4px;
    padding-bottom: 3px; border-bottom: 1px solid var(--rule);
  }
  .identity__tagline { font-size: 9.5px; color: var(--ink-grey); letter-spacing: 2.2px; margin-top: 3px; }
  .person { position: absolute; left: 40px; top: 135px; }
  .person__name { font-size: 19px; color: var(--ink-blue); }
  .person__role { font-size: 13.5px; color: var(--ink-red); margin-top: 1px; }
  .contact { position: absolute; left: 40px; top: 192px; font-size: 12.5px; color: var(--ink-grey); line-height: 19px; }
  .contact__city { margin-bottom: 4px; }
  .contact__row { display: flex; align-items: center; gap: 8px; }
  .contact__row svg { width: 13px; height: 13px; fill: var(--ink-blue); flex: none; }
</style>
</head>
<body>
<main class="sheet">
  <section class="card card--back" aria-label="Card back">
    <div class="back-mark">
      <span class="back-mark__dot"></span>
      <span class="back-mark__name">Larkspur Holdings LLC</span>
    </div>
    <p class="back-web">www.lhllc.example</p>
  </section>

  <section class="card card--front" aria-label="Card front">
    <div class="front-disc"></div>
    <div class="identity">
      <p class="identity__company">Larkspur Holdings LLC</p>
      <p class="identity__tagline">Global Business Strategists</p>
    </div>
    <div class="person">
      <p class="person__name">Tobias Ferrant Aldo</p>
      <p class="person__role">Chief Strategist</p>
    </div>
    <div class="contact">
      <p class="contact__city">New York, USA.</p>
      <p class="contact__row">
        <svg viewBox="0 0 16 16" aria-hidden="true"><path d="M2 5c0-2 2-3 6-3s6 1 6 3v1h-3V4.5H5V6H2z M4 8h8l1.5 6h-11z"/></svg>
        555.014.2207</p>
      <p class="contact__row">
        <svg viewBox="0 0 16 16" aria-hidden="true"><path d="M4 1h8v14H4z M5.5 2.5v10h5v-10z"/></svg>
        555.018.3391</p>
      <p class="contact__row">
        <svg viewBox="0 0 16 16" aria-hidden="true"><path d="M1 3h14v10H1z M2.5 4.5 8 9l5.5-4.5z"/></svg>
        tobias@lhllc.example</p>
      <p class="contact__row">
        <svg viewBox="0 0 16 16" aria-hidden="true"><circle cx="8" cy="8" r="7"/><path d="M1 8h14M8 1v14" stroke="#fff" stroke-width="1"/></svg>
        www.lhllc.example</p>
    </div>
  </section>
</main>
</body>
</html>
```